TOASTED COCONUT CHIPS

My company is a food company specialised in coconut products. The subject project is to design the package bag and respective simple shipping case for toasted coconut chips for two flavors: one is original and the other is cinnamon. I also need a logo design for the brand "pimlo".

I would like the bag looks simple, classy and attractive. Or the other way that it could look cute and fun.

The design will include two flavors: original/sea salt and cinnamon
The design need to be fit in 40g pouch bag and 20g bag.
Need the design of the bag and subsequently the shipping case.

Target Market(s)

age 8 to 40
sell in cafeteria and vending machine

Industry/Entity Type

It Company

Logo Text

simple and direct

Requirements
Must have
• golden coconut chips picture on the front side.
• the bag should looks clean but attractive.
• Otherwise, it has to be very colourful to attract eye balls.
• I need the design can be fit in a 40g pouch and 20g cutie size bag
Should not have
• Should not look Asian food.

```html
<!DOCTYPE html>
<html lang="en">
<head>
<meta charset="utf-8">
<title>pimlo toasted coconut chips – sea salt pouch</title>
<link rel="stylesheet" href="https://fonts.googleapis.com/css2?family=Questrial&family=Crimson+Text:ital@1&family=Yanone+Kaffeesatz:wght@500&display=swap">
<style>
  :root {
    --sun-yellow: #f6d417;
    --sun-yellow-light: #fbe65a;
    --gold-dark: #b98a06;
    --gold-mid: #e8bb12;
    --gold-light: #fff0a0;
    --band-white: #ffffff;
    --ink: #2a2626;
    --salt-brown: #a4683f;
    --badge-red: #e3303a;
    --chip-dark: #2b1d14;
    --chip-mid: #6b4a32;
    --chip-gold: #d9b07a;
    --chip-cream: #f3e2c4;
  }
  html, body {
    margin: 0;
    padding: 0;
    overflow: hidden;
    background: #e9f6f6;
  }
  .pouch-front {
    display: block;
    width: 900px;
    height: 1200px;
  }
  .brand-name {
    font-family: "Questrial", sans-serif;
    font-size: 200px;
    fill: var(--ink);
  }
  .flavour-name {
    font-family: "Questrial", sans-serif;
    font-size: 96px;
    fill: var(--salt-brown);
  }
  .product-type {
    font-family: "Questrial", sans-serif;
    font-size: 50px;
    fill: var(--ink);
  }
  .badge-text {
    font-family: "Crimson Text", serif;
    font-style: italic;
    font-size: 34px;
    fill: #ffffff;
  }
  .pack-note {
    font-family: "Yanone Kaffeesatz", sans-serif;
    font-weight: 500;
    font-size: 36px;
    fill: var(--ink);
    text-decoration: underline;
  }
</style>
</head>
<body>
<svg class="pouch-front" viewBox="0 0 900 1200" xmlns="http://www.w3.org/2000/svg">
  <defs>
    <linearGradient id="top-yellow" x1="0" y1="0" x2="1" y2="1">
      <stop offset="0" stop-color="var(--sun-yellow-light)"/>
      <stop offset="1" stop-color="var(--sun-yellow)"/>
    </linearGradient>
    <linearGradient id="gold-seal" x1="0" y1="0" x2="1" y2="0">
      <stop offset="0" stop-color="var(--gold-dark)"/>
      <stop offset="0.25" stop-color="var(--gold-light)"/>
      <stop offset="0.5" stop-color="var(--gold-mid)"/>
      <stop offset="0.75" stop-color="var(--gold-light)"/>
      <stop offset="1" stop-color="var(--gold-dark)"/>
    </linearGradient>
    <radialGradient id="chips-photo" cx="0.5" cy="0.45" r="0.7">
      <stop offset="0" stop-color="var(--chip-cream)"/>
      <stop offset="0.35" stop-color="var(--chip-gold)"/>
      <stop offset="0.7" stop-color="var(--chip-mid)"/>
      <stop offset="1" stop-color="var(--chip-dark)"/>
    </radialGradient>
  </defs>

  <!-- yellow upper field -->
  <rect class="upper-field" x="0" y="0" width="900" height="1200" fill="url(#top-yellow)"/>

  <!-- diagonal band and product area -->
  <g class="diagonal-band" transform="translate(0 720) rotate(-27.6)">
    <rect class="chips-photo" x="-300" y="257" width="1700" height="900" fill="url(#chips-photo)"
          role="img" aria-label="Photo of golden toasted coconut chips in a bowl"/>
    <rect class="band-white" x="-300" y="0" width="1700" height="257" fill="var(--band-white)"/>
    <line class="perforation-top" x1="-300" y1="0" x2="1400" y2="0"
          stroke="var(--sun-yellow)" stroke-width="14" stroke-linecap="round" stroke-dasharray="0 20"/>
    <line class="perforation-bottom" x1="-300" y1="257" x2="1400" y2="257"
          stroke="var(--chip-dark)" stroke-width="14" stroke-linecap="round" stroke-dasharray="0 20"/>

    <text class="brand-name" x="40" y="170">pimlo</text>
    <text class="flavour-name" x="215" y="240">sea salt</text>
    <text class="product-type" x="640" y="62">toasted</text>
    <text class="product-type" x="660" y="110">coconut</text>
    <text class="product-type" x="680" y="158">chips</text>
  </g>

  <!-- claim badge -->
  <g class="claim-badge" transform="translate(200 330) rotate(-20)">
    <ellipse rx="175" ry="92" fill="var(--badge-red)"/>
    <ellipse rx="160" ry="80" fill="none" stroke="var(--sun-yellow)" stroke-width="2"/>
    <text class="badge-text" x="0" y="-6" text-anchor="middle">premium coconuts</text>
    <text class="badge-text" x="0" y="32" text-anchor="middle">toasted to perfection.</text>
  </g>

  <!-- seals -->
  <rect class="seal-top" x="0" y="0" width="900" height="60" fill="url(#gold-seal)"/>
  <rect class="seal-bottom" x="0" y="1115" width="900" height="85" fill="url(#gold-seal)"/>
  <text class="pack-note" x="450" y="1170" text-anchor="middle">Packed Unique home-compostable eco bags</text>
</svg>
</body>
</html>
```